Eyecatching Design for Car price comparison website - read now! :)

We need a cool fresh responsive design for our website www.fahrzeug-preis-ermitteln.de ... it is a website where you can calculate the worth of your old used car for free.

We like the layout of http://www.gebrauchtwagenzentrale.de/ or https://www.qorm.de very much.

We want the customer to quickly understand how the website works and what he can do. The customer should develop trust to our calculation.

Our old Color green should be included.
Updates

Project Deadline Extended
Reason: Hey guys, some more designs are welcome... Now coded project! :)

Target Market(s)

People that want to sell their cars, men and women

Industry/Entity Type

Car Dealer

Coding

Coded - Design and coding required

Number of Pages Required

3 page

Font styles to use
Sans Serif

Colors
acd036

Requirements
Must have
• Attractive, Trusting, Responsive, Focus on functionality
Should not have
• To be to close to http://www.gebrauchtwagenzentrale.de/ or https://www.qorm.de

```html
<!DOCTYPE html>
<html lang="de">
<head>
<meta charset="utf-8">
<title>Fahrzeug-Preis-Ermitteln</title>
<link rel="stylesheet" href="https://fonts.googleapis.com/css2?family=Montserrat:wght@400;500;600&family=Open+Sans:ital,wght@0,400;0,600;1,400&display=swap">
<style>
:root{
  --green:#acd036;
  --green-dark:#8cb51f;
  --green-btn-top:#b6d94a;
  --green-btn-bottom:#86b21c;
  --text:#444;
  --muted:#888;
  --light:#f2f2f2;
  --grey-band:#ececec;
  --footer:#4a4a4a;
  --white:#fff;
  --orange:#e0702a;
}
*{box-sizing:border-box;margin:0;padding:0}
html,body{width:1200px;height:2507px;overflow:hidden}
body{font-family:"Open Sans",Arial,sans-serif;color:var(--text);background:var(--white);position:relative}
.abs{position:absolute}
h1,h2,h3,.heading{font-family:"Montserrat",Arial,sans-serif;font-weight:400}

/* header */
.site-header{position:absolute;top:0;left:0;width:1200px;height:90px;background:var(--white)}
.brand{position:absolute;left:117px;top:28px;font-family:"Montserrat",sans-serif;font-weight:600;font-size:24px;color:var(--green-dark);display:flex;align-items:center;gap:10px}
.brand-dot{width:14px;height:14px;border-radius:50%;background:var(--green)}
.main-nav a{position:absolute;top:36px;font-size:15px;color:#666;text-decoration:none}
.phone{position:absolute;left:920px;top:32px;font-family:"Montserrat",sans-serif;font-weight:500;font-size:19px;color:#222;display:flex;align-items:center;gap:8px}

/* hero */
.hero{position:absolute;top:90px;left:0;width:1200px;height:445px;
  background:linear-gradient(180deg,#9fc2e2 0%,#b9d0e0 22%,#7e9a3c 32%,#9aae50 60%,#b3b86a 100%)}
.hero-people{position:absolute;left:0;top:0;width:560px;height:445px;background:linear-gradient(90deg,#5a1f1f 0%,#8a4d42 35%,#c99b80 70%,rgba(170,170,100,0) 100%)}
.hero-title{position:absolute;left:104px;top:232px;font-family:"Montserrat",sans-serif;font-size:35px;line-height:42px;color:var(--white);font-weight:500}
.slider-dots{position:absolute;left:558px;top:406px;display:flex;gap:6px}
.slider-dots span{width:18px;height:18px;border-radius:50%;background:var(--white)}
.slider-dots span:first-child{background:transparent;border:2px solid var(--white)}
.calc-box{position:absolute;left:758px;top:85px;width:322px;height:276px;background:rgba(245,242,232,.93);padding:24px 22px}
.calc-box h2{font-size:22px;color:#333;margin-bottom:14px}
.select{height:37px;background:var(--white);border:1px solid #d6d6d6;font-size:13px;color:#666;padding:0 14px;display:flex;align-items:center;justify-content:space-between;margin-bottom:8px}
.select-row{display:flex;gap:6px}
.select-row .select{flex:1}
.btn{display:inline-flex;align-items:center;justify-content:center;background:linear-gradient(180deg,var(--green-btn-top),var(--green-btn-bottom));color:var(--white);font-family:"Montserrat",sans-serif}
.calc-box .btn{width:100%;height:46px;font-size:18px;margin-top:4px}

/* intro */
.intro{position:absolute;top:535px;left:0;width:1200px;height:351px}
.intro h1{position:absolute;left:130px;top:50px;font-size:29px;line-height:35px;color:#333}
.intro p{position:absolute;left:130px;width:480px;font-size:13px;line-height:21px;color:var(--muted)}
.intro .btn{position:absolute;left:131px;top:264px;width:137px;height:38px;font-size:15px}
.device{position:absolute;left:643px;top:38px;width:393px;height:272px}
.device-screen{position:absolute;left:40px;top:0;width:313px;height:230px;background:#1c1c1c;border-radius:12px;padding:14px}
.device-screen .screen{width:100%;height:100%;background:linear-gradient(180deg,#8a9a4a 0%,#a7b666 45%,#f5f5f5 46%,#fff 100%)}
.device-base{position:absolute;left:0;top:230px;width:393px;height:16px;background:linear-gradient(180deg,#e4e4e4,#a9a9a9);border-radius:0 0 40px 40px}

/* how */
.how{position:absolute;top:886px;left:0;width:1200px;height:339px;background:var(--green)}
.how-title{position:absolute;top:24px;left:0;width:1200px;text-align:center;font-size:29px;color:var(--white);font-family:"Montserrat",sans-serif}
.how-line{position:absolute;top:45px;height:1px;width:80px;background:rgba(255,255,255,.7)}
.step{position:absolute;top:92px;width:320px;text-align:center;color:var(--white)}
.step-icon{width:106px;height:106px;border-radius:50%;border:4px solid var(--white);margin:0 auto;display:flex;align-items:center;justify-content:center}
.step h3{font-size:19px;margin-top:20px;font-weight:500}
.step p{font-size:13px;line-height:21px;margin-top:6px;color:rgba(255,255,255,.85)}

/* auto value */
.value{position:absolute;top:1225px;left:0;width:1200px;height:359px}
.value-photo{position:absolute;left:124px;top:53px;width:401px;height:243px;background:linear-gradient(135deg,#6f8a3c 0%,#c5ccd0 45%,#f1f1f1 70%,#9aa0a3 100%)}
.value h2{position:absolute;left:555px;top:54px;font-size:27px;color:#333}
.value p{position:absolute;left:555px;width:520px;font-size:12.5px;line-height:21px;color:var(--muted)}
.value .btn{position:absolute;left:558px;top:253px;width:137px;height:38px;font-size:15px}

/* why */
.why{position:absolute;top:1584px;left:0;width:1200px;height:415px;background:linear-gradient(90deg,var(--grey-band) 0%,var(--grey-band) 45%,#dfe2e6 62%,#c7d3e4 100%)}
.why-photo{position:absolute;right:0;top:0;width:560px;height:415px;background:linear-gradient(90deg,rgba(236,236,236,1) 0%,rgba(200,212,230,.6) 30%,#6f8fc4 60%,#c2ccd8 100%)}
.why h2{position:absolute;left:124px;top:66px;font-size:27px;color:#333}
.why p{position:absolute;left:124px;top:112px;width:520px;font-size:12.5px;line-height:21px;color:var(--muted)}
.why ul{position:absolute;left:124px;top:190px;list-style:none}
.why li{display:flex;align-items:center;gap:12px;font-size:13px;color:#666;height:33px}

/* reviews */
.reviews{position:absolute;top:1999px;left:0;width:1200px;height:382px;background:linear-gradient(180deg,#3e5a1e 0%,#6d8a3a 40%,#8a8a5c 75%,#4a4a32 100%)}
.reviews h2{position:absolute;top:30px;left:0;width:1200px;text-align:center;font-size:29px;color:var(--white)}
.review{position:absolute;top:86px;width:304px;height:171px;background:var(--white);padding:26px 28px;text-align:center;font-style:italic;font-size:12.5px;line-height:23px;color:#888}
.review::after{content:"";position:absolute;left:140px;bottom:-12px;border:12px solid transparent;border-bottom:0;border-top-color:var(--white)}
.author{position:absolute;top:275px;display:flex;align-items:center;gap:10px;color:var(--white)}
.avatar{width:56px;height:56px;border-radius:50%;background:linear-gradient(135deg,#d9c3b0,#9a7f6d);border:3px solid var(--white)}
.author b{display:block;font-weight:400;font-size:15px}
.author span{font-size:13px;color:rgba(255,255,255,.85)}
.arrow{position:absolute;top:166px}

/* footer */
.site-footer{position:absolute;top:2381px;left:0;width:1200px;height:126px;background:var(--footer)}
.footer-nav a{position:absolute;top:37px;font-size:15px;color:var(--white);text-decoration:none}
.copyright{position:absolute;left:125px;top:69px;font-size:11px;color:#bbb}
.social{position:absolute;top:29px;width:34px;height:34px;border-radius:50%;background:#333}
</style>
</head>
<body>

<header class="site-header">
  <div class="brand"><span class="brand-dot"></span>Fahrzeug-Preis-Ermitteln</div>
  <nav class="main-nav">
    <a style="left:490px">Home</a>
    <a style="left:572px">Autowert</a>
    <a style="left:678px">Auto Liste</a>
    <a style="left:785px">Impressum</a>
  </nav>
  <div class="phone">
    <svg width="18" height="18" viewBox="0 0 24 24"><path fill="#acd036" d="M6.6 10.8c1.4 2.8 3.8 5.1 6.6 6.6l2.2-2.2c.3-.3.7-.4 1-.2 1.1.4 2.3.6 3.6.6.6 0 1 .4 1 1V20c0 .6-.4 1-1 1C10.6 21 3 13.4 3 4c0-.6.4-1 1-1h3.5c.6 0 1 .4 1 1 0 1.3.2 2.5.6 3.6.1.3 0 .7-.2 1z"/></svg>
    030 555 0147
  </div>
</header>

<section class="hero">
  <div class="hero-people" role="img" aria-label="Foto: Familie sitzt im offenen Kofferraum eines roten Autos auf einer Wiese"></div>
  <div class="hero-title">Donec dictum lectus<br>Proin nulla arcu nonummy</div>
  <div class="slider-dots"><span></span><span></span><span></span><span></span></div>
  <form class="calc-box">
    <h2>Calculate Old Car Cost</h2>
    <div class="select">Select Make <svg width="14" height="8"><path d="M1 1l6 6 6-6" stroke="#888" fill="none" stroke-width="1.5"/></svg></div>
    <div class="select">Select Model <svg width="14" height="8"><path d="M1 1l6 6 6-6" stroke="#888" fill="none" stroke-width="1.5"/></svg></div>
    <div class="select-row">
      <div class="select">Select Year <svg width="14" height="8"><path d="M1 1l6 6 6-6" stroke="#888" fill="none" stroke-width="1.5"/></svg></div>
      <div class="select">Type <svg width="14" height="8"><path d="M1 1l6 6 6-6" stroke="#888" fill="none" stroke-width="1.5"/></svg></div>
    </div>
    <span class="btn">Calculate Now</span>
  </form>
</section>

<section class="intro">
  <h1>Calculate the worth of your<br>old used car for free</h1>
  <p style="top:132px">Fusce ultricies orci ac feugiat suscipit leo massa sodales velit et scelerisque mi tortor at ipsum cligula augue bibendum accumsan</p>
  <p style="top:186px">vestibulum ut commodo a mi Morbi ornare gravida elit Integer congue augue et malesuada iaculis ipsum dui aliquet felis at cursus magna nisl nec elit Praesent elementum elit at tellus nec ultricies sit amet porttitor</p>
  <span class="btn">Learn More</span>
  <div class="device">
    <div class="device-screen"><div class="screen" role="img" aria-label="Vorschau der Startseite auf einem Laptop-Bildschirm"></div></div>
    <div class="device-base"></div>
  </div>
</section>

<section class="how">
  <div class="how-line" style="left:418px"></div>
  <div class="how-title">How it Works</div>
  <div class="how-line" style="left:702px"></div>
  <div class="step" style="left:134px">
    <div class="step-icon"><svg width="48" height="48" viewBox="0 0 48 48" fill="none" stroke="#fff" stroke-width="3"><rect x="6" y="8" width="36" height="32" rx="2"/><path d="M6 15h36M13 22h22M13 28h14M13 34h18"/></svg></div>
    <h3>Register Our Website</h3>
    <p>cursus magna nisl nec elit Praesent ele<br>mentum elit at tellus ultricies</p>
  </div>
  <div class="step" style="left:442px">
    <div class="step-icon"><svg width="54" height="40" viewBox="0 0 54 40" fill="#fff"><path d="M12 6h30l6 12h4v12h-4v6h-8v-6H14v6H6v-6H2V18h4z"/><rect x="14" y="10" width="26" height="8" fill="#acd036"/><circle cx="13" cy="24" r="3" fill="#acd036"/><circle cx="41" cy="24" r="3" fill="#acd036"/></svg></div>
    <h3>Input your Car Detials</h3>
    <p>cursus magna nisl nec elit Praesent ele<br>mentum elit at tellus ultricies</p>
  </div>
  <div class="step" style="left:747px">
    <div class="step-icon"><svg width="48" height="48" viewBox="0 0 48 48" fill="none" stroke="#fff" stroke-width="3"><path d="M10 6h22l6 6v14M10 6v36h16"/><path d="M16 16h14M16 22h14M16 28h8"/><circle cx="35" cy="35" r="8" fill="#fff"/><path d="M31 35l3 3 5-6" stroke="#acd036"/></svg></div>
    <h3>Get Your Car Cost</h3>
    <p>cursus magna nisl nec elit Praesent ele<br>mentum elit at tellus ultricies</p>
  </div>
</section>

<section class="value">
  <div class="value-photo" role="img" aria-label="Foto: Familie schaut lachend aus einem weißen Auto"></div>
  <h2>Der Auto Wert</h2>
  <p style="top:100px">Wer sich einen Gebrauchtwagen kaufen oder sein altes Auto verkaufen will, kommt nicht darum herum sich eine realistische Vorstellung über den Preis zu machen. Oftmals ist eine objektive Bewertung eines Gebrauchtwagens kostenpflichtig.</p>
  <p style="top:172px">Aber es gibt auch kostenlose Autowert-Rechner oder Auto-Listen welche dieselben Leistungen erbringen können wie ein kostenpflichtige Angebote. Und natürlich mit deutlich weniger Umständen und Zeitaufwand.</p>
  <span class="btn">Learn More</span>
</section>

<section class="why">
  <div class="why-photo" role="img" aria-label="Foto: lächelnder Mann arbeitet am Laptop im Büro"></div>
  <h2>Why Choose Us</h2>
  <p>Wer sich einen Gebrauchtwagen kaufen oder sein altes Auto verkaufen will, kommt nicht darum herum sich eine realistische Vorstellung über den Preis zu machen. Oftmals ist eine objektive Bewertung eines Gebrauchtwagens kostenpflichtig.</p>
  <ul>
    <li><svg width="16" height="16" viewBox="0 0 16 16"><circle cx="8" cy="8" r="8" fill="#e0702a"/><path d="M4.5 8l2.5 2.5 4.5-5" stroke="#fff" stroke-width="2" fill="none"/></svg>Fusce ultricies orci ac feugiat suscipit</li>
    <li><svg width="16" height="16" viewBox="0 0 16 16"><circle cx="8" cy="8" r="8" fill="#e0702a"/><path d="M4.5 8l2.5 2.5 4.5-5" stroke="#fff" stroke-width="2" fill="none"/></svg>Leo massa sodales velit et scelerisque mi tortor</li>
    <li><svg width="16" height="16" viewBox="0 0 16 16"><circle cx="8" cy="8" r="8" fill="#e0702a"/><path d="M4.5 8l2.5 2.5 4.5-5" stroke="#fff" stroke-width="2" fill="none"/></svg>At ipsum cligula augue bibendum</li>
    <li><svg width="16" height="16" viewBox="0 0 16 16"><circle cx="8" cy="8" r="8" fill="#e0702a"/><path d="M4.5 8l2.5 2.5 4.5-5" stroke="#fff" stroke-width="2" fill="none"/></svg>Pccumsan vestibulum ut commodo a mi Morbi</li>
  </ul>
</section>

<section class="reviews" role="img" aria-label="Hintergrundfoto: Landstraße unter grünen Bäumen">
  <h2>Customer Review</h2>
  <svg class="arrow" style="left:90px" width="20" height="34" viewBox="0 0 20 34"><path d="M17 3L4 17l13 14" stroke="#fff" stroke-width="4" fill="none"/></svg>
  <svg class="arrow" style="left:1092px" width="20" height="34" viewBox="0 0 20 34"><path d="M3 3l13 14L3 31" stroke="#fff" stroke-width="4" fill="none"/></svg>

  <div class="review" style="left:130px">Eget tempor cursus neque mi consectetuer mi a ultricies massa est sed nisl Class aptent taciti sociosqu ad litora torquent per conubia nostra per inceptos hymenaeos Proin nulla arcu nonummy</div>
  <div class="review" style="left:454px">Curabitur vel mi sit amet magna malesuada ultrices Ut nisi erat fermentum vel congue id euismod in elit Fusce ultricies orci ac feugiat suscipit leo massa sodale</div>
  <div class="review" style="left:778px">Eget tempor cursus neque mi consectetuer mi a ultricies massa est sed nisl Class aptent taciti sociosqu ad litora torquent per conubia nostra per inceptos hymenaeos Proin nulla arcu</div>

  <div class="author" style="left:197px"><div class="avatar" role="img" aria-label="Porträtfoto Kunde"></div><div><b>By Author Name</b><span>City Name</span></div></div>
  <div class="author" style="left:520px"><div class="avatar" role="img" aria-label="Porträtfoto Kunde"></div><div><b>By Author Name</b><span>City Name</span></div></div>
  <div class="author" style="left:844px"><div class="avatar" role="img" aria-label="Porträtfoto Kundin"></div><div><b>By Author Name</b><span>City Name</span></div></div>
</section>

<footer class="site-footer">
  <nav class="footer-nav">
    <a style="left:125px">Home</a>
    <a style="left:207px">Autowert</a>
    <a style="left:313px">Auto Liste</a>
    <a style="left:423px">Impressum</a>
    <a style="left:544px">Support</a>
    <a style="left:637px">Contact</a>
  </nav>
  <div class="copyright">© 2016 Company Name &nbsp;All right reserved &nbsp;Term of Use</div>
  <span class="social" style="left:905px"></span>
  <span class="social" style="left:951px"></span>
  <span class="social" style="left:998px"></span>
  <span class="social" style="left:1045px"></span>
</footer>

</body>
</html>
```